IT Company, Needs new Logo and Letterhead Design

We need a Letterhead and possible a new logo for an existing IT Company. We are not happy with our current Letterhead that we are using in our quotes etc. We are happy to change our logo if required. We will upload our current logo and letterhead and look forward to getting some examples. We provide Server, Workstation and network support.

Target Market(s)

Small to Medium Sized Businesses.

Industry/Entity Type

It Company

Requirements
Must have
• Ability to edit the letterhead at a later date. Will need the source files for editing once approved.
Nice to have
• Same colour scheme, but we are open to suggestions.

```html
<!DOCTYPE html>
<html lang="en">
<head>
<meta charset="utf-8">
<title>Kestrel Network Services – Letterhead</title>
<link href="https://fonts.googleapis.com/css2?family=Arimo:wght@400;700&display=swap" rel="stylesheet">
<style>
  :root {
    --backdrop: #cccccc;
    --paper: #ffffff;
    --navy: #0b2a5c;
    --amber: #f7941d;
    --footer-text: #ffffff;
  }
  * { margin: 0; padding: 0; box-sizing: border-box; }
  html, body {
    width: 1200px;
    height: 1000px;
    overflow: hidden;
    background: var(--backdrop);
    font-family: "Arimo", Arial, sans-serif;
  }
  .letterhead {
    position: absolute;
    left: 288px;
    top: 57px;
    width: 644px;
    height: 885px;
    background: var(--paper);
  }
  .brand {
    position: absolute;
    right: 50px;
    top: 118px;
    transform: translateY(-50%);
    display: flex;
    align-items: center;
    gap: 8px;
  }
  .brand-dot {
    width: 16px;
    height: 16px;
    border-radius: 50%;
    background: var(--amber);
  }
  .brand-name {
    color: var(--navy);
    font-weight: 700;
    font-size: 15px;
    line-height: 1.15;
    text-align: right;
  }
  .footer-band {
    position: absolute;
    left: 0;
    bottom: 0;
    width: 100%;
    height: 30px;
    background: var(--navy);
  }
  .contact {
    position: absolute;
    top: 50%;
    transform: translateY(-50%);
    color: var(--footer-text);
    font-size: 9px;
    white-space: nowrap;
  }
  .contact-phone { left: 128px; }
  .contact-email { left: 242px; }
  .contact-support { left: 408px; }
</style>
</head>
<body>
  <main class="letterhead">
    <header class="brand">
      <span class="brand-dot"></span>
      <span class="brand-name">Kestrel Network<br>Services</span>
    </header>
    <footer class="footer-band">
      <span class="contact contact-phone">Ph: +1300 555 014 2290</span>
      <span class="contact contact-email">E: info@kestrelnetworks.com.au</span>
      <span class="contact contact-support">Support: support@kestrelnetworks.com.au</span>
    </footer>
  </main>
</body>
</html>
```